Business Card Design

I need a business card for my tutoring service. Key elements on front are its contact details and visual appeal with these three points: All aspects of literacy and numeracy, 'Bright Steps Program Plus' provider and Prep-readiness sessions
Updates

contact me by email on danafor7@quillmail.net as I'm having issues with other address at times. Thanks

:) 

Target Market(s)

People with children

Industry/Entity Type

Tutoring

Contact Information for Business Card

Dana Forsythe Educational Consultant
12 Tamarind Rise
Larkfield 4512
0471 388 912

Requirements
Nice to have
• Something related to education. On the back of the card, my business name and phone number again, along with: spelling, reading, writing, comprehension, oral language, listening skills

```html
<!DOCTYPE html>
<html lang="en">
<head>
<meta charset="utf-8">
<title>Dana Forsythe – Educational Consultant business card</title>
<link href="https://fonts.googleapis.com/css2?family=Open+Sans:ital,wght@0,400;0,700;1,400&display=swap" rel="stylesheet">
<style>
  :root {
    --bg: #e9e9e7;
    --card: #ffffff;
    --ink: #232323;
    --yellow: #e3e86b;
    --blue: #70c1d3;
    --orange: #d6654f;
    --shadow: rgba(0,0,0,0.12);
  }
  * { box-sizing: border-box; margin: 0; padding: 0; }
  html, body {
    width: 1200px; height: 800px; overflow: hidden;
    background: var(--bg);
    font-family: "Open Sans", Arial, sans-serif;
    color: var(--ink);
  }
  .sheet {
    position: relative; width: 1200px; height: 800px;
    display: flex; align-items: center; justify-content: center; gap: 50px;
  }
  .card {
    position: relative; width: 525px; height: 300px;
    background: var(--card); overflow: hidden;
    box-shadow: 0 6px 20px var(--shadow);
  }
  .card p, .card h1 { position: absolute; z-index: 1; white-space: nowrap; }

  /* front */
  .front .shape-square { position: absolute; left: 40px; top: 80px; width: 84px; height: 46px; background: var(--yellow); }
  .front .shape-circle { position: absolute; left: 150px; top: 24px; width: 64px; height: 64px; border-radius: 50%; background: var(--blue); }
  .front .shape-triangle { position: absolute; left: 380px; top: 22px; }
  .front .name { left: 92px; top: 36px; font-size: 28px; font-weight: 700; line-height: 1.1; }
  .front .role { left: 92px; top: 84px; font-size: 19px; line-height: 1.2; }
  .front .tagline { left: 40px; top: 122px; font-size: 22px; line-height: 1.2; }
  .band {
    left: 0; width: 100%; height: 28px;
    display: flex; align-items: center; font-size: 15px;
  }
  .band-yellow { background: var(--yellow); }
  .band-blue { background: var(--blue); }
  .band-orange { background: var(--orange); }
  .front .band { padding-left: 92px; }
  .front .band-yellow { top: 170px; }
  .front .band-blue { top: 198px; }
  .front .band-orange { top: 226px; }

  /* back */
  .back .icon-book { position: absolute; left: 110px; top: 58px; width: 82px; height: 82px; background: var(--yellow); }
  .back .icon-children { position: absolute; left: 222px; top: 48px; width: 84px; height: 84px; border-radius: 50%; background: var(--blue); }
  .back .icon-cap { position: absolute; left: 340px; top: 40px; }
  .back .band { justify-content: center; }
  .back .band-yellow { top: 178px; font-style: italic; font-size: 14.5px; }
  .back .band-blue { top: 206px; font-size: 16px; }
  .back .band-orange { top: 234px; font-size: 16px; }
</style>
</head>
<body>
<main class="sheet">
  <section class="card front" aria-label="Business card front">
    <div class="shape-square"></div>
    <div class="shape-circle"></div>
    <svg class="shape-triangle" width="82" height="80" viewBox="0 0 82 80" aria-hidden="true">
      <polygon points="0,0 82,0 30,80" fill="var(--orange)"/>
    </svg>
    <h1 class="name">Dana Forsythe</h1>
    <p class="role">Educational Consultant</p>
    <p class="tagline">All aspects of literacy and numeracy</p>
    <p class="band band-yellow">danafor7@quillmail.net</p>
    <p class="band band-blue">12 Tamarind Rise Larkfield 4512</p>
    <p class="band band-orange">0471 388 912</p>
  </section>

  <section class="card back" aria-label="Business card back">
    <div class="icon-book" role="img" aria-label="Open book illustration on yellow square"></div>
    <div class="icon-children" role="img" aria-label="Playing children silhouettes in blue circle"></div>
    <svg class="icon-cap" width="96" height="94" viewBox="0 0 96 94" role="img" aria-label="Graduation cap on orange triangle">
      <polygon points="0,0 96,30 22,94" fill="var(--orange)"/>
    </svg>
    <p class="band band-yellow">Spelling • Reading • Writing • Comprehension • Oral language • Listening skills</p>
    <p class="band band-blue">'Bright Steps Program Plus' provider</p>
    <p class="band band-orange">Prep-readiness sessions</p>
  </section>
</main>
</body>
</html>
```